Business Card for a Child Psychologist

I am a psychologist working with children and families and need a business card to give to clients and referral sources. I see children of all ages, so it should not look too young - as it will be for older children too. My work involves dealing with families in difficult situations, likes divorce, or with issues such as depression and anxiety. The design should communicate that I provide an open,warm, friendly, and caring atmosphere. I want to convey a sense of hope and positivity. Using colors like blues, purples

Target Market(s)

Families, doctors, family law attorneys

Industry/Entity Type

Psychology

Contact Information for Business Card

Dana Whitlow, Ph.D.
462 W. Marbury Row, Suite 2100
Chicago, Illinois 60688
312-555-0173
drdanajwhitlow@mailvista.example

Font styles to use
Script

Requirements
Must have
• A Logo to go with the details of my contact information.
Should not have
• Nothing in the shape of a brain. Nothing sad, or that looks too clinical.

```html
<!DOCTYPE html>
<html lang="en">
<head>
<meta charset="UTF-8">
<title>Dana Whitlow, Ph.D. — Business Card</title>
<link href="https://fonts.googleapis.com/css2?family=Jost:wght@400;500&family=Montserrat:wght@400;500&display=swap" rel="stylesheet">
<style>
  :root {
    --page-bg: #2b2b2d;
    --violet-light: #8f78bd;
    --violet-mid: #5a48a0;
    --indigo-deep: #2c2a78;
    --brand-purple: #6650a8;
    --brand-blue: #3c5ea8;
    --ink: #3a3a3e;
    --card-white: #ffffff;
    --mark-white: rgba(255, 255, 255, 0.92);
  }
  * { box-sizing: border-box; margin: 0; padding: 0; }
  html, body {
    width: 1200px; height: 900px; overflow: hidden;
    background: var(--page-bg);
    font-family: "Jost", Arial, sans-serif;
  }
  .canvas { position: relative; width: 1200px; height: 900px; }

  .card {
    position: absolute;
    width: 580px; height: 332px;
    border-radius: 4px;
    box-shadow: 0 10px 30px rgba(0, 0, 0, 0.45);
    overflow: hidden;
  }

  /* Back side */
  .card--back {
    left: 560px; top: 60px;
    background: linear-gradient(115deg, var(--violet-light) 0%, var(--violet-mid) 55%, var(--indigo-deep) 100%);
    display: flex; flex-direction: column; align-items: center; justify-content: center;
    color: var(--mark-white);
  }
  .wordmark { display: flex; align-items: center; gap: 12px; }
  .wordmark__dot {
    width: 22px; height: 22px; border-radius: 50%;
    background: currentColor; flex: none;
  }
  .wordmark__name { font-weight: 500; font-size: 40px; line-height: 1; }
  .wordmark__degree { font-size: 0.45em; margin-left: 6px; }
  .card--back .tagline {
    margin-top: 14px;
    font-family: "Montserrat", Arial, sans-serif;
    font-size: 15px; letter-spacing: 3.5px; text-transform: uppercase;
  }

  /* Front side */
  .card--front {
    left: 60px; top: 470px;
    background: var(--card-white);
    color: var(--ink);
  }
  .card--front .identity {
    position: absolute; left: 36px; top: 34px;
    color: var(--brand-purple);
  }
  .card--front .wordmark__dot { width: 16px; height: 16px; }
  .card--front .wordmark__name { font-size: 28px; }
  .card--front .tagline {
    margin-top: 6px; margin-left: 28px;
    font-family: "Montserrat", Arial, sans-serif;
    font-size: 11px; letter-spacing: 2.4px; text-transform: uppercase;
    color: var(--ink);
  }
  .divider {
    position: absolute; left: 36px; right: 36px; height: 1.5px;
    background: var(--brand-purple);
  }
  .divider--top { top: 124px; }
  .divider--bottom { top: 296px; left: 330px; }

  .contact-list {
    position: absolute; left: 36px; top: 146px;
    list-style: none; font-size: 16.5px; line-height: 1.55;
  }
  .contact-list li { display: flex; align-items: flex-start; gap: 10px; }
  .contact-list .icon {
    width: 20px; height: 20px; flex: none; margin-top: 3px;
    border-radius: 50%; background: var(--brand-purple);
    display: flex; align-items: center; justify-content: center;
  }
  .contact-list .icon--mail { background: var(--brand-blue); }
  .contact-list .indent { padding-left: 30px; }

  .signature {
    position: absolute; right: 36px; top: 236px; text-align: left;
  }
  .signature__name {
    font-size: 22px; font-weight: 500; color: var(--brand-purple);
    text-transform: uppercase; line-height: 1.1;
  }
  .signature__role { font-size: 16px; color: var(--ink); }
</style>
</head>
<body>
<main class="canvas">

  <section class="card card--back" aria-label="Card back">
    <div class="wordmark">
      <span class="wordmark__dot"></span>
      <span class="wordmark__name">Dana Whitlow<span class="wordmark__degree">Ph.D</span></span>
    </div>
    <p class="tagline">Clinical Psychologist</p>
  </section>

  <section class="card card--front" aria-label="Card front">
    <div class="identity">
      <div class="wordmark">
        <span class="wordmark__dot"></span>
        <span class="wordmark__name">Dana Whitlow<span class="wordmark__degree">Ph.D</span></span>
      </div>
      <p class="tagline">Clinical Psychologist</p>
    </div>

    <div class="divider divider--top"></div>

    <ul class="contact-list">
      <li>
        <span class="icon" aria-hidden="true">
          <svg width="11" height="11" viewBox="0 0 24 24"><path fill="#fff" d="M6.6 10.8a15.1 15.1 0 0 0 6.6 6.6l2.2-2.2c.3-.3.7-.4 1-.2 1.1.4 2.3.6 3.6.6.6 0 1 .4 1 1V20c0 .6-.4 1-1 1A17 17 0 0 1 3 4c0-.6.4-1 1-1h3.5c.6 0 1 .4 1 1 0 1.3.2 2.5.6 3.6.1.3 0 .7-.2 1z"/></svg>
        </span>
        312 - 555 - 0173
      </li>
      <li>
        <span class="icon icon--mail" aria-hidden="true">
          <svg width="11" height="11" viewBox="0 0 24 24"><path fill="#fff" d="M2 5h20v14H2z"/><path fill="none" stroke="#3c5ea8" stroke-width="2" d="M2 5l10 8 10-8"/></svg>
        </span>
        drdanajwhitlow@mailvista.example
      </li>
      <li>
        <span class="icon" aria-hidden="true">
          <svg width="11" height="11" viewBox="0 0 24 24"><path fill="#fff" d="M12 2a7 7 0 0 0-7 7c0 5 7 13 7 13s7-8 7-13a7 7 0 0 0-7-7zm0 9.5A2.5 2.5 0 1 1 12 6.5a2.5 2.5 0 0 1 0 5z"/></svg>
        </span>
        462 W. Marbury Row, Suite 2100
      </li>
      <li class="indent">Chicago, Illinois 60688</li>
    </ul>

    <div class="signature">
      <p class="signature__name">Dana Whitlow</p>
      <p class="signature__role">Clinical Psychologist</p>
    </div>
    <div class="divider divider--bottom"></div>
  </section>

</main>
</body>
</html>
```